1 page Venture WheelOn Investor Sheet. This is given to individuals as well as corporations

we are focusing on the "Slip Sheet" (or) "Investor
Sheet'. We will be using this one page document to introduce folks to our organization and open conversations on monetary donations. Must have an ask for $50 to sponsor a child.

Some of the things we are looking for are the overall style/design.
Content should include...

1) Overall: Who we are, What we do, Why or How we do it (I also am
including a copy of our Mission and values statement)

2) Our ask - via the missing link (or) $50 to sponsor a child...How can I help?

3) Maybe a testimonial or two

4) Metrics / Statistics from our programs (may pull some of this from annual report for now)

Target Market(s)

Individual and Corporate

Industry/Entity Type

Non-Profit

Font styles to use
Other font styles liked:
• please use style guide for correct fonts

Requirements
Must have
• 1) Overall: Who we are, What we do, Why or How we do it (I also am including a copy of our Mission and values statement)
• 2) Our ask – via the missing link (or) $50 to sponsor a child…How can I help?
• 3) Maybe a testimonial or two
• 4) Metrics / Statistics from our programs (may pull some of this from annual report for now)
• 5) logo
• 6) photos of kids on bikes
• 7) our color scheme and fonts per style guideline

```html
<!DOCTYPE html>
<html lang="en">
<head>
<meta charset="utf-8">
<title>Venture WheelOn – Investor Sheet</title>
<link rel="stylesheet" href="https://fonts.googleapis.com/css2?family=Delius&family=Open+Sans:wght@700&family=Roboto+Condensed:wght@400;700&family=Oswald:wght@600&display=swap">
<style>
  :root {
    --orange: #f07d1a;
    --band-orange: #ef7a16;
    --sky: #4cbfe2;
    --lime: #b7cf3c;
    --grass: #b4cf46;
    --ink: #1f1f1f;
    --paper: #ffffff;
  }
  * { box-sizing: border-box; margin: 0; padding: 0; }
  html, body { width: 849px; height: 1200px; overflow: hidden; background: var(--paper); }
  .sheet { position: relative; width: 849px; height: 1200px; overflow: hidden; background: var(--paper); font-family: "Roboto Condensed", "Arial Narrow", sans-serif; }

  .brand { position: absolute; left: 52px; top: 150px; width: 230px; text-align: center; }
  .brand-mark { display: inline-block; width: 22px; height: 22px; border-radius: 50%; background: var(--sky); margin-bottom: 10px; }
  .brand-name { font-family: "Oswald", sans-serif; font-weight: 600; font-size: 38px; line-height: 1.05; color: var(--sky); text-transform: uppercase; letter-spacing: 1px; }

  .photo { position: absolute; }
  .photo-fill { position: absolute; inset: 0; }
  .photo-frame { position: absolute; inset: -6px; pointer-events: none; overflow: visible; }
  .photo--riders { left: 358px; top: 45px; width: 438px; height: 255px; }
  .photo--riders .photo-fill { background: linear-gradient(180deg, #c9d9e6 0%, #8fae5c 38%, #6c8d3a 60%, #b8a27c 100%); }
  .photo--helmet { left: 544px; top: 700px; width: 278px; height: 382px; }
  .photo--helmet .photo-fill { background: linear-gradient(170deg, #cfd6d9 0%, #e9a9c4 45%, #4fb3a9 70%, #e77fb0 100%); }

  .tagline-band { position: absolute; left: 0; top: 339px; width: 849px; height: 67px; background: var(--band-orange); display: flex; align-items: center; justify-content: center; }
  .tagline { font-family: "Open Sans", sans-serif; font-weight: 700; font-size: 19.5px; color: var(--paper); }

  .section-title { position: absolute; font-family: "Delius", cursive; font-size: 42px; line-height: 1; letter-spacing: 1px; }
  .section-title--who { left: 70px; top: 447px; color: var(--orange); }
  .section-title--what { left: 553px; top: 572px; color: var(--sky); }
  .section-title--help { left: 70px; top: 823px; color: var(--lime); }

  .who-copy { position: absolute; left: 352px; top: 434px; width: 455px; font-size: 12.6px; line-height: 1.32; font-weight: 700; color: var(--orange); text-align: center; }

  .what-box { position: absolute; left: 54px; top: 530px; width: 762px; height: 131px; }
  .what-box svg { position: absolute; inset: 0; overflow: visible; }
  .what-copy { position: absolute; left: 72px; top: 549px; width: 458px; font-size: 12.6px; line-height: 1.33; color: var(--sky); text-align: justify; text-align-last: center; }

  .motto { position: absolute; left: 70px; top: 695px; display: flex; gap: 0; }
  .motto-item { position: relative; font-family: "Delius", cursive; font-size: 37px; color: var(--orange); line-height: 1; }
  .motto-item svg { display: block; margin-bottom: 10px; }
  .motto-item--ride { width: 122px; }
  .motto-item--rebuild { width: 162px; }

  .help-intro { position: absolute; left: 71px; top: 893px; width: 420px; font-size: 13.2px; line-height: 1.3; font-weight: 700; color: var(--sky); }
  .sponsor-list { position: absolute; left: 71px; top: 943px; font-size: 12.6px; color: var(--orange); }
  .sponsor-row { display: flex; margin-bottom: 12px; }
  .sponsor-label { width: 113px; font-weight: 700; }
  .sponsor-detail { line-height: 1.35; }

  .grass { position: absolute; left: 0; top: 1050px; width: 849px; height: 150px; }
  .contact { position: absolute; left: 0; top: 1107px; width: 849px; text-align: center; font-size: 12.4px; line-height: 1.55; color: var(--ink); }
</style>
</head>
<body>
<main class="sheet">

  <div class="brand">
    <span class="brand-mark"></span>
    <div class="brand-name">Venture<br>WheelOn</div>
  </div>

  <figure class="photo photo--riders">
    <div class="photo-fill" role="img" aria-label="Photo of four children riding bicycles along a country path"></div>
    <svg class="photo-frame" width="450" height="267" viewBox="0 0 450 267">
      <path d="M4 5 L446 3 L445 263 L3 262 Z" fill="none" stroke="var(--sky)" stroke-width="2.2"/>
      <path d="M8 2 L443 7 L448 258 L7 265 Z" fill="none" stroke="var(--sky)" stroke-width="1.2"/>
    </svg>
  </figure>

  <div class="tagline-band">
    <p class="tagline">Help a child find their passion to success and open the door to a great future!</p>
  </div>

  <h2 class="section-title section-title--who">who we are</h2>
  <p class="who-copy">Each year, Venture WheelOn reaches out to the community to raise the funds necessary to help over 1,500 children strive for success. It is our commitment to keep our costs low and opportunities for children high, and that is where we need your help. A $50 sponsorship provides a child with a bicycle, helmet, lock, and the opportunity to achieve success and gain confidence in their abilities.</p>

  <div class="what-box">
    <svg width="762" height="131" viewBox="0 0 762 131">
      <path d="M2 3 L760 1 L758 129 L4 130 Z" fill="none" stroke="var(--lime)" stroke-width="2.2"/>
      <path d="M6 0 L756 5 L761 126 L0 127 Z" fill="none" stroke="var(--lime)" stroke-width="1.2"/>
    </svg>
  </div>
  <p class="what-copy">Our bicycle program runs year round. We collect bikes from individuals, groups, or coporations. Individual help has come from contact with schools and churches. A huge support has come from the residents of Cedar Hollow, Colorado. Cedar Hollow schools and churches have actively supported our bike program. Corporations encourage their employees, tenants or vendors to participate by donating a new or used bike to our program.</p>
  <h2 class="section-title section-title--what">what we do</h2>

  <div class="motto">
    <div class="motto-item motto-item--ride">
      <svg width="40" height="34" viewBox="0 0 40 34" fill="none" stroke="var(--orange)" stroke-width="2.4" stroke-linecap="round" stroke-linejoin="round">
        <circle cx="9" cy="24" r="7"/><circle cx="31" cy="24" r="7"/>
        <path d="M9 24 L16 12 L27 12 L31 24 M16 12 L21 24 L27 12 M14 8 L19 8 M27 12 L25 6 L29 5"/>
      </svg>
      ride
    </div>
    <div class="motto-item motto-item--rebuild">
      <svg width="40" height="34" viewBox="0 0 40 34" fill="none" stroke="var(--orange)" stroke-width="2.4" stroke-linecap="round" stroke-linejoin="round">
        <path d="M8 6 a6 6 0 1 0 6 8 L30 28 a3 3 0 0 0 4 -4 L20 10 a6 6 0 0 0 -8 -6 l3 4 -2 3 -4 -1 Z"/>
      </svg>
      rebuild
    </div>
    <div class="motto-item motto-item--repeat">
      <svg width="40" height="34" viewBox="0 0 40 34" fill="none" stroke="var(--orange)" stroke-width="2.4" stroke-linejoin="round">
        <path d="M20 31 C8 22 3 16 3 10 A8 8 0 0 1 20 7 A8 8 0 0 1 37 10 C37 16 32 22 20 31 Z"/>
      </svg>
      repeat
    </div>
  </div>

  <h2 class="section-title section-title--help">how you can help</h2>
  <p class="help-intro">You may help fill the gap by becoming a MISSING LINK donor or sponsor...here is how</p>
  <div class="sponsor-list">
    <div class="sponsor-row">
      <span class="sponsor-label">Sponsor a child:</span>
      <span class="sponsor-detail">$50 annual donation sponsors a child<br>$50 monthly donation sponsors 12 children each year</span>
    </div>
    <div class="sponsor-row">
      <span class="sponsor-label">Sponsor a school:</span>
      <span class="sponsor-detail">$15,000 sponsors an entire school's Dream Bike program</span>
    </div>
  </div>

  <figure class="photo photo--helmet">
    <div class="photo-fill" role="img" aria-label="Photo of a young girl having her bike helmet fastened at a community event"></div>
    <svg class="photo-frame" width="290" height="394" viewBox="0 0 290 394">
      <path d="M3 4 L287 2 L286 390 L4 391 Z" fill="none" stroke="var(--sky)" stroke-width="2.2"/>
      <path d="M7 1 L284 6 L289 387 L1 388 Z" fill="none" stroke="var(--sky)" stroke-width="1.2"/>
    </svg>
  </figure>

  <svg class="grass" width="849" height="150" viewBox="0 0 849 150" preserveAspectRatio="none">
    <path d="M0 40 Q120 18 240 34 T480 30 T720 28 T849 36 L849 150 L0 150 Z" fill="var(--grass)"/>
  </svg>

  <address class="contact" style="font-style:normal">
    4710 Larkspur Ave. Suite 220, Pine Bluff, CO 80999<br>
    www.VentureWheelOn.org<br>
    admin@venturewheelon.org
  </address>

</main>
</body>
</html>
```